Label Design for an exciting food startup introducing millets to North America!

We need a label for Millet grains (and millet flour after design is finalized for the grains because it will be very similar except for the description) Looking for a clean, minimalistic design. Modern feel. We are a social enterprise introducing millet based products to North American Market and we cater to the customers who are health conscious, eat plant-based foods, may have gluten allergies and are looking for a healthy substitutes for carbohydrate-rich foods.Millets are a great alternative for rice/barley/couscous/quinoa. Very nutritious grain!Our big audacious goal is to make Millets the new Quinoa in the next 3 years!!! More information about the company can be found on the website koshafoods.comMore information in the brief attached.

Target Market(s)

Women (75%) and men (25%) aged 21-60 who are health conscious, want to eat vegan/plant based foods, willing to experiment with new foods. They care about the environment and doing good while choosing products that are good for them and the planet.

Industry/Entity Type

Food Production

Colors

Designer to choose colors to be used in the design.

Requirements
Must have
• Covered in the project brief attached
Nice to have
Should not have

```html
<!DOCTYPE html>
<html lang="en">
<head>
<meta charset="utf-8">
<title>Brendavale Foods – Millet Grain Pouch Label</title>
<link href="https://fonts.googleapis.com/css2?family=Alegreya:wght@400&family=Patrick+Hand&family=Permanent+Marker&family=Roboto:wght@400;700&display=swap" rel="stylesheet">
<style>
  :root{
    --bg:#f7ece2;
    --paper:#f4f4f2;
    --orange:#e8742a;
    --brand:#d2693b;
    --green:#7ab648;
    --ink:#161616;
    --grain-light:#f3d35a;
    --grain-dark:#d9a21e;
    --red:#d52b1e;
  }
  *{box-sizing:border-box;margin:0;padding:0}
  html,body{width:1200px;height:900px;overflow:hidden;background:var(--bg)}
  .canvas{position:relative;width:1200px;height:900px}
  .label{position:absolute;top:140px;width:438px;height:640px;background:var(--paper);overflow:hidden;color:var(--ink)}
  .label--front{left:162px}
  .label--back{left:664px}
  .abs{position:absolute;z-index:2}
  .art{position:absolute;z-index:1}
  .brand{font-family:"Alegreya",serif;color:var(--brand);font-size:22px;display:flex;align-items:center;gap:8px;white-space:nowrap}
  .brand-dot{width:14px;height:14px;border-radius:50%;background:var(--brand);flex:none}
  .product-title{font-family:"Permanent Marker",cursive;font-weight:400;font-size:54px;line-height:62px;left:36px;top:224px;z-index:3}
  .window{left:44px;top:392px;width:358px;height:124px;border-radius:4px;background:radial-gradient(ellipse at 40% 40%,var(--grain-light),var(--grain-dark))}
  .claims{list-style:none;font-family:"Permanent Marker",cursive;color:#fff;font-size:16px;line-height:31px;left:282px;top:296px;white-space:nowrap}
  .benefits{font-family:"Patrick Hand",cursive;left:54px;top:518px;font-size:15px;line-height:17px;transform:rotate(4deg);transform-origin:left top;white-space:nowrap}
  .benefit-health{color:var(--green)}
  .benefit-nutrients{margin-top:9px;color:var(--ink)}
  .net-weight{font-family:"Permanent Marker",cursive;font-size:17px;left:278px;top:574px;white-space:nowrap}
  .story-band{left:26px;top:144px;width:234px;height:36px;background:var(--green);color:#fff;display:flex;align-items:center;gap:6px;padding-left:12px;font-family:"Permanent Marker",cursive;white-space:nowrap}
  .story-band b{font-weight:400;font-size:15px}
  .story-band span{font-size:7px;line-height:9px}
  .soup{left:12px;top:200px;width:104px;height:148px;border-radius:50%;background:radial-gradient(circle at 50% 45%,#c9a36a,#8e6535)}
  .recipes-title{font-family:"Permanent Marker",cursive;font-weight:400;font-size:12px;line-height:14px;letter-spacing:1px;left:140px;top:206px;white-space:nowrap}
  .recipe-text{font-family:"Patrick Hand",cursive;font-style:italic;font-size:8.4px;line-height:10.2px;left:142px;top:248px;width:108px}
  .nutrition-table{left:262px;top:248px;width:146px;border:1px solid var(--ink);padding:3px 4px;font-family:"Roboto",sans-serif;font-size:6.6px;line-height:8.4px}
  .nutrition-table h3{font-size:11px;line-height:12px}
  .nutrition-table .row{display:flex;justify-content:space-between;border-top:0.6px solid var(--ink)}
  .nutrition-table .thick{border-top:2px solid var(--ink)}
  .nutrition-table .cols{display:flex;justify-content:flex-end;gap:14px;font-size:5.5px}
  .nutrition-table .foot{font-size:5.2px;line-height:6.4px;border-top:2px solid var(--ink);padding-top:2px}
  .facts{font-family:"Permanent Marker",cursive;font-size:7.5px;line-height:10px;left:40px;white-space:nowrap}
  .maker{font-family:"Patrick Hand",cursive;font-style:italic;font-size:8px;line-height:9.6px;left:46px;top:522px;width:118px}
  .web{font-family:"Permanent Marker",cursive;font-size:6.8px;left:50px;top:605px}
  .badge{top:548px;text-align:center;font-family:"Permanent Marker",cursive;font-size:8.5px;line-height:10px;white-space:nowrap}
  .badge .mark{margin:0 auto 4px}
  .badge--canada{left:172px}
  .badge--canada .mark{width:32px;height:32px;background:var(--red)}
  .badge--recycle{left:244px;top:562px}
  .badge--recycle .mark{width:26px;height:26px;border-radius:50%;background:var(--green)}
</style>
</head>
<body>
<main class="canvas">

  <section class="label label--front">
    <svg class="art" style="left:148px;top:0" width="290" height="96" role="img" aria-label="Scattered golden millet grains">
      <defs><linearGradient id="grainFront" x1="0" y1="0" x2="0" y2="1"><stop offset="0" stop-color="#d9a21e"/><stop offset="1" stop-color="#f3d35a"/></linearGradient></defs>
      <path d="M60 0 H290 V40 C240 60 200 66 150 70 C110 72 70 60 40 40 C30 25 45 8 60 0Z" fill="url(#grainFront)"/>
      <circle cx="20" cy="40" r="4" fill="#e9bd3c"/><circle cx="54" cy="86" r="4" fill="#e9bd3c"/><circle cx="120" cy="92" r="4" fill="#e9bd3c"/><circle cx="230" cy="74" r="4" fill="#e9bd3c"/>
    </svg>

    <svg class="art" style="left:110px;top:216px" width="320" height="350" role="img" aria-label="Orange watercolour splash with a sketched millet stalk">
      <path d="M70 40 C110 10 160 30 200 20 C250 5 290 30 300 70 C320 120 300 150 316 190 C320 230 290 240 270 250 L80 250 C40 240 10 200 20 150 C30 100 40 60 70 40Z M240 250 C270 270 280 310 250 340 C220 350 200 320 205 290 Z" fill="var(--orange)"/>
    </svg>

    <div class="brand abs" style="left:36px;top:168px"><span class="brand-dot"></span>Brendavale Foods</div>

    <h1 class="product-title abs">MILLET<br>GRAIN</h1>

    <div class="window abs" role="img" aria-label="Clear window showing the hulled yellow millet inside"></div>

    <ul class="claims abs">
      <li>RAW,</li><li>VEGAN AND</li><li>GLUTEN-FREE</li>
    </ul>

    <div class="benefits abs">
      <p class="benefit-health">• Low Glycemic Index<br>• Diabetic friendly</p>
      <p class="benefit-nutrients">• Source of Protein,<br>• Fibre and minerals</p>
    </div>

    <p class="net-weight abs">450 g (1 lb)</p>
  </section>

  <section class="label label--back">
    <svg class="art" style="left:0;top:0" width="280" height="104" role="img" aria-label="Scattered golden millet grains">
      <defs><linearGradient id="grainBack" x1="0" y1="0" x2="0" y2="1"><stop offset="0" stop-color="#d9a21e"/><stop offset="1" stop-color="#f3d35a"/></linearGradient></defs>
      <path d="M0 0 H240 C250 30 220 60 170 72 C120 84 60 90 0 96Z" fill="url(#grainBack)"/>
      <circle cx="200" cy="84" r="4" fill="#e9bd3c"/><circle cx="250" cy="96" r="4" fill="#e9bd3c"/><circle cx="150" cy="100" r="4" fill="#e9bd3c"/>
    </svg>

    <svg class="art" style="left:0;top:92px" width="140" height="314" role="img" aria-label="Orange watercolour splash">
      <path d="M0 10 C40 0 90 20 110 60 C130 110 120 170 136 220 C140 270 110 300 70 310 C40 314 10 300 0 290Z" fill="var(--orange)"/>
    </svg>

    <div class="story-band abs"><b>OUR STORY:</b><span>PRODUCED THROUGH A PARTNERSHIP<br>WITH FARMERS IN INDIA</span></div>

    <div class="soup abs" role="img" aria-label="Bowl of millet vegetable soup"></div>

    <div class="brand abs" style="left:268px;top:186px;font-size:18px"><span class="brand-dot"></span>Brendavale Foods</div>

    <h2 class="recipes-title abs">SIMPLE &amp; EASY<br>MILLET RECIPES!</h2>

    <p class="recipe-text abs">This is Lorem Ipsum. Proin gravida nibh vel velit auctor aliquet. Aenean sollicitudin, lorem quis bibendum auctor, nisi elit consequat ipsum, nec sagittis sem nibh id elit. Duis sed odio sit amet nibh vulputate cursus a sit amet mauris. Morbi accumsan ipsum velit. Nam nec tellus a odio tincidunt auctor a ornare odio. Sed non mauris vitae erat consequat auctor eu in elit. Class aptent taciti sociosqu ad litora torquent per conubia</p>

    <div class="nutrition-table abs">
      <h3>Valeur nutritive</h3>
      <p>pour MD (MM)<br>(environ MD préparé)</p>
      <div class="cols thick"><span>Tel que vendu</span><span>Préparé</span></div>
      <div class="row" style="font-size:9px;line-height:12px"><b>Calories</b><span>####&nbsp;&nbsp;&nbsp;####</span></div>
      <div class="cols thick"><span>% valeur quotidienne*</span></div>
      <div class="row"><span><b>Lipides</b> ## g<br>&nbsp;saturés ## g<br>&nbsp;+ trans ## g</span><span>## %&nbsp;&nbsp;&nbsp;## %<br><br>## %</span></div>
      <div class="row"><span><b>Glucides</b> ## g<br>&nbsp;Fibres ## g<br>&nbsp;Sucres ## g</span><span><br>## %&nbsp;&nbsp;&nbsp;## %<br>## %&nbsp;&nbsp;&nbsp;## %</span></div>
      <div class="row"><span><b>Protéines</b> ## g</span></div>
      <div class="row"><span><b>Cholestérol</b> ### mg</span></div>
      <div class="row thick"><span><b>Sodium</b> #### mg</span><span>## %&nbsp;&nbsp;&nbsp;## %</span></div>
      <div class="row thick"><span>Potassium #### mg</span><span>## %&nbsp;&nbsp;&nbsp;## %</span></div>
      <div class="row"><span>Calcium #### mg</span><span>## %&nbsp;&nbsp;&nbsp;## %</span></div>
      <div class="row"><span>Fer ## mg</span><span>## %&nbsp;&nbsp;&nbsp;## %</span></div>
      <p class="foot">* Teneur de l'aliment tel que vendu.<br>MD d'aliment ajouté, ### Calories, ## g lipides, ## g glucides, ## g protéines.<br>* 5% ou moins c'est peu, 15% ou plus c'est beaucoup</p>
    </div>

    <p class="facts abs" style="top:462px">INGREDIENTS: WHOLE GRAIN MILLETS</p>
    <p class="facts abs" style="top:482px">ORIGIN: INDIA</p>

    <p class="maker abs">Manufactured By<br>This is Lorem Ipsum. Proin gravida nibh vel velit auctor aliquet. Aenean sollicitudin, lorem quis bibendum<br><br>consequat ipsum, nec sagittis sem nibh id elit. Duis sed odio sit amet</p>

    <p class="web abs">WWW.BRENDAVALE.COM</p>

    <div class="badge badge--canada abs"><div class="mark"></div>PACKAGED IN<br>CANADA</div>
    <div class="badge badge--recycle abs"><div class="mark"></div>RECYCLE</div>
  </section>

</main>
</body>
</html>
```